Handout for attendees of educational seminar

I provide educational workshops on how to give technical presentations at conferences to scientists and engineers. My company is called Frame Your Research (www.FrameYourResearch.example). I would like a double sided, half page size flyer that can be used as a handout for attendees of my workshops. On one side of the flyer, they will get top tips for creating their next presentation. On the other side, they will get my photo, bio, and contact information. I have uploaded a draft of a full page design I made myself. I'd like the copy of the tips to remain the same, but everything else is flexible.

Target Market(s)

scientists, engineers, technical professionals

Font styles to use
Serif
Sans Serif

Requirements
Must have
• my photo (I've provided two options to choose from depending on colors...photo on side 2 only), my logo, flyer needs to be half page in size (5.5" x 8.5"), needs to be double sided, One side has the "tips" and the other side has my personal details (see attached page for copy).
Nice to have
• I like the use of icons on the "tips" side of the flyer.

```html
<!DOCTYPE html>
<html lang="en">
<head>
<meta charset="utf-8">
<title>Frame Your Research – Quick Tips Handout</title>
<link href="https://fonts.googleapis.com/css2?family=Open+Sans:wght@400;600;700;800&family=Raleway:wght@300;400&family=Bitter:ital,wght@1,300;1,400&family=Source+Sans+3:wght@400;600&display=swap" rel="stylesheet">
<style>
  :root{
    --green:#8cc63f;
    --blue:#5bbbe0;
    --charcoal:#4b4848;
    --charcoal-deep:#3c3a3a;
    --box-grey:#6d6d70;
    --paper:#f6f6f5;
    --ink:#4a4a4a;
    --page:#e9e9e7;
    --white:#ffffff;
  }
  *{box-sizing:border-box;margin:0;padding:0}
  html,body{width:826px;height:1200px;overflow:hidden;background:var(--page)}
  body{position:relative;font-family:"Open Sans",Arial,sans-serif}
  .card{position:absolute;left:41px;width:800px;height:620px;transform:scale(.93);transform-origin:0 0;background:var(--paper);overflow:hidden;box-shadow:0 2px 6px rgba(0,0,0,.12)}
  .card--tips{top:15px}
  .card--bio{top:608px}

  /* ---------- Tips side ---------- */
  .hero{position:absolute;left:0;top:0;width:800px;height:280px}
  .hero-kicker{position:absolute;left:30px;top:32px;color:var(--green);font-family:"Open Sans",sans-serif;font-weight:400;font-size:27px;letter-spacing:.5px}
  .hero-title{position:absolute;left:30px;top:62px;color:var(--white);font-weight:800;font-size:57px;letter-spacing:.5px}
  .hero-rule{position:absolute;left:32px;top:146px;width:318px;height:2px;background:var(--blue)}
  .hero-tagline{position:absolute;left:30px;top:159px;color:var(--blue);font-weight:700;font-size:13.5px}
  .brand{position:absolute;right:22px;top:12px;width:200px;text-align:center}
  .brand-mark{display:block;width:74px;height:74px;border-radius:50%;background:var(--charcoal-deep);margin:0 auto 10px}
  .brand-name{font-family:"Raleway",sans-serif;font-weight:300;font-size:25px;color:var(--green);white-space:nowrap}

  .tips{position:absolute;left:18px;top:300px;width:764px;display:flex;justify-content:space-between}
  .tip{position:relative;width:242px;height:140px;margin-top:86px;background:var(--box-grey);border-radius:5px;padding:32px 10px 0;color:var(--white)}
  .tip-icon{position:absolute;left:50%;top:-89px;width:108px;height:108px;margin-left:-54px;border-radius:50%;background:var(--blue);border:5px solid var(--paper);display:flex;align-items:center;justify-content:center}
  .tip-title{text-align:center;font-weight:700;font-size:13.5px;letter-spacing:.2px;margin-bottom:8px}
  .tip-text{font-size:8.4px;line-height:1.3;text-align:justify;letter-spacing:-.15px}
  .tip-hint{margin-top:11px;font-size:8.2px;line-height:1.35;color:var(--blue);text-align:justify;letter-spacing:-.15px}
  .tip-hint b{font-weight:700}
  .tip-hint--bold{font-weight:700}

  .contact-band{position:absolute;left:0;top:562px;width:800px;height:40px;background:var(--green);display:flex;justify-content:center;align-items:center;gap:44px;color:var(--white);font-size:14px}
  .contact-item{display:flex;align-items:center;gap:5px}
  .contact-dot{width:13px;height:13px;border-radius:50%;border:1.5px solid var(--white);display:inline-block}

  /* ---------- Bio side ---------- */
  .portrait{position:absolute;left:0;top:0;width:360px;height:420px}
  .bio-brand{position:absolute;left:60px;top:352px;width:280px;text-align:center}
  .bio-brand .brand-mark{width:82px;height:82px;margin-bottom:6px;border:3px solid var(--paper)}
  .bio-brand .brand-name{font-size:26px}
  .bio-quote{position:absolute;left:40px;top:490px;width:320px;text-align:center;font-family:"Bitter",Georgia,serif;font-style:italic;font-weight:300;font-size:21px;line-height:1.45;color:var(--ink)}
  .bio{position:absolute;left:400px;top:98px;width:378px;font-family:"Source Sans 3",Arial,sans-serif;color:var(--ink);font-size:12.8px;line-height:1.34}
  .bio-heading{font-family:"Bitter",Georgia,serif;font-style:italic;font-weight:400;color:var(--blue);font-size:18px;margin-bottom:10px}
  .bio p{text-align:justify;margin-bottom:15px}
</style>
</head>
<body>

<!-- ===== Side 1: Quick tips ===== -->
<section class="card card--tips">
  <svg class="hero" viewBox="0 0 800 280" aria-hidden="false">
    <defs>
      <linearGradient id="heroShade" x1="0" y1="0" x2="1" y2="0">
        <stop offset="0" stop-color="#4a4747"/>
        <stop offset="1" stop-color="#575454"/>
      </linearGradient>
      <linearGradient id="stagePhoto" x1="0" y1="0" x2="1" y2="1">
        <stop offset="0" stop-color="#6a6767"/>
        <stop offset=".5" stop-color="#8a8786"/>
        <stop offset="1" stop-color="#4c4949"/>
      </linearGradient>
      <clipPath id="heroClip"><path d="M0 0H800V228Q470 290 0 212Z"/></clipPath>
    </defs>
    <path d="M0 216Q430 300 800 232V246Q430 296 0 226Z" fill="#c9c9c9"/>
    <g clip-path="url(#heroClip)">
      <rect width="800" height="280" fill="url(#heroShade)"/>
      <rect x="320" y="0" width="330" height="280" fill="url(#stagePhoto)" opacity=".85" role="img" aria-label="Photo of the speaker presenting on a conference stage"/>
    </g>
    <path d="M230 268Q540 262 800 224V232Q540 274 230 268Z" fill="var(--green)"/>
  </svg>
  <div class="hero-kicker">FRAME YOUR RESEARCH</div>
  <h1 class="hero-title">QUICK TIPS</h1>
  <div class="hero-rule"></div>
  <p class="hero-tagline">Science not communicated is science not done!</p>
  <div class="brand">
    <span class="brand-mark"></span>
    <div class="brand-name">Clara Whitfield</div>
  </div>

  <div class="tips">
    <article class="tip">
      <div class="tip-icon">
        <svg width="60" height="52" viewBox="0 0 60 52" fill="none" stroke="#fff" stroke-width="2.4" aria-hidden="true">
          <rect x="10" y="4" width="40" height="12" rx="2"/>
          <line x1="16" y1="16" x2="16" y2="22"/><line x1="44" y1="16" x2="44" y2="22"/>
          <g fill="#fff" stroke="none">
            <circle cx="14" cy="30" r="5"/><circle cx="26" cy="30" r="5"/><circle cx="38" cy="30" r="5"/><circle cx="50" cy="30" r="5"/>
            <circle cx="20" cy="43" r="5"/><circle cx="32" cy="43" r="5"/><circle cx="44" cy="43" r="5"/>
          </g>
        </svg>
      </div>
      <h2 class="tip-title">BE AUDIENCE CENTERED</h2>
      <p class="tip-text">Your ability to be successful as a speaker depends upon your ability to make your audience successful.</p>
      <p class="tip-hint tip-hint--bold">TIP: Be an interpreter of your work, not a reporter. Always connect each piece of technical info to a “So what?” point.</p>
    </article>
    <article class="tip">
      <div class="tip-icon">
        <svg width="56" height="54" viewBox="0 0 56 54" fill="none" stroke="#fff" stroke-width="2.4" aria-hidden="true">
          <rect x="6" y="4" width="44" height="30" rx="2"/>
          <line x1="18" y1="34" x2="12" y2="50"/><line x1="38" y1="34" x2="44" y2="50"/><line x1="28" y1="34" x2="28" y2="48"/>
          <path d="M14 25l4-4M14 21l4 4M26 25l4-4M26 21l4 4M38 14a3 3 0 1 0 .1 0"/>
          <path d="M18 14q8-6 16 0" stroke-dasharray="2 2"/>
        </svg>
      </div>
      <h2 class="tip-title">FILTER &amp; FOCUS</h2>
      <p class="tip-text">When you try to share everything, you share nothing.</p>
      <p class="tip-hint" style="margin-top:24px">TIP: Start your planning with the “view” you want your audience to have at the end of the talk. Then ask yourself “What would they need to know in order to get there?”</p>
    </article>
    <article class="tip">
      <div class="tip-icon">
        <svg width="62" height="62" viewBox="0 0 62 62" fill="none" stroke="#fff" stroke-width="2.4" aria-hidden="true">
          <circle cx="31" cy="31" r="24" stroke-dasharray="4 3"/>
          <path d="M9 31q22-20 44 0q-22 20-44 0Z"/>
          <circle cx="31" cy="31" r="7" fill="#fff"/>
        </svg>
      </div>
      <h2 class="tip-title">SHOW YOUR SCIENCE</h2>
      <p class="tip-text">Your slides should do something for you that your words cannot. This means make your slides VISUAL not VERBAL.</p>
      <p class="tip-hint tip-hint--bold">TIP: Avoid bullet points (seriously!). Have a brief take-away message at the top of each slide and support it with visual evidence.</p>
    </article>
  </div>

  <footer class="contact-band">
    <span class="contact-item"><span class="contact-dot"></span>clara@frameyourresearch.example</span>
    <span class="contact-item"><span class="contact-dot"></span>www.FrameYourResearch.example</span>
  </footer>
</section>

<!-- ===== Side 2: About ===== -->
<section class="card card--bio">
  <svg class="portrait" viewBox="0 0 360 420">
    <defs>
      <linearGradient id="portraitTone" x1="0" y1="0" x2="1" y2="1">
        <stop offset="0" stop-color="#c9b7a3"/>
        <stop offset=".55" stop-color="#a98668"/>
        <stop offset="1" stop-color="#2f8a5a"/>
      </linearGradient>
    </defs>
    <circle cx="120" cy="170" r="244" fill="var(--blue)"/>
    <circle cx="114" cy="176" r="238" fill="var(--paper)"/>
    <circle cx="112" cy="178" r="236" fill="#9a9a9a"/>
    <circle cx="108" cy="172" r="234" fill="url(#portraitTone)" role="img" aria-label="Portrait photo of Clara Whitfield"/>
  </svg>
  <div class="bio-brand">
    <span class="brand-mark"></span>
    <div class="brand-name">Clara Whitfield</div>
  </div>
  <p class="bio-quote">Science not communicated is<br>science not done.</p>

  <div class="bio">
    <h2 class="bio-heading">Meet Clara</h2>
    <p>Clara Whitfield is on a mission: to transform how scientists, engineers, and technical professionals present their work. That’s because she believes that even the best technical ideas are destined to remain undiscovered unless presented in a clear and compelling way that sparks innovation and drives adoption.</p>
    <p>For a decade, she’s traveled around the world to work with Global 100 corporations, institutions and universities, teaching the proven strategies she’s mastered through her consulting work and during her time as a faculty member at Northfield State University.</p>
    <p>Clara is internationally known for her popular Summit Stage talk entitled "Speak Clearly to Me" which has over 2 million views (and counting!).</p>
    <p>Teams that work with Clara get the practical skills and natural confidence they need to immediately shift their “information dump”-style presentations into ones that are meaningful, engaging, and inspire people to take action.</p>
    <p>Clara is the founder of Frame Your Research, a consulting company that provides on-site group workshops, conference keynotes, and 1:1 coaching.</p>
  </div>

  <footer class="contact-band">
    <span class="contact-item"><span class="contact-dot"></span>clara@frameyourresearch.example</span>
    <span class="contact-item"><span class="contact-dot"></span>www.FrameYourResearch.example</span>
  </footer>
</section>

</body>
</html>
```